Brava Stone Oven Kitchen (restaurant)

Restaurant with a cool vibe.
We need a refresh of existing site. Appealing to a hip crowd of 25 or older age bracket (mid price to high small town). Constant changes food and cocktail menu. A vibing atmosphere with jazz funk hip music.
Must be able to scale for any device… phone/mobile device super important.
Instagram: @Brava.Linwell
Website: bravalinwell.example

Target Market(s)

25-55 age group

Number of Pages Required

1 page

Font styles to use
Sans Serif

Requirements
Must have
• Simple to navigate. Simplicity is the key to all sophistication.

Links/Buttons
Menu
Gift Cards
Reservations
Take Out
Contact Us
Should not have
• Please, nothing generic looking… no cookie cutter look. Originality

```html
<!DOCTYPE html>
<html lang="en">
<head>
<meta charset="utf-8">
<title>Brava Stone Oven Kitchen</title>
<link rel="stylesheet" href="https://fonts.googleapis.com/css2?family=Poppins:wght@500;600;700&family=Open+Sans:wght@400;600&display=swap">
<style>
:root{
  --red:#d50f25;
  --red-deep:#c20d22;
  --ink:#1a1a1a;
  --text:#333;
  --grey:#f0f0f0;
  --footer:#1f1f1f;
  --white:#fff;
}
*{box-sizing:border-box;margin:0;padding:0}
html,body{width:1200px;height:3857px;overflow:hidden}
body{position:relative;font-family:"Open Sans",Arial,sans-serif;color:var(--text);background:var(--white)}
.abs{position:absolute}
.heading{font-family:"Poppins",Arial,sans-serif;font-weight:700;text-transform:uppercase;color:var(--ink)}
.heading .accent{color:var(--red)}
.rule{position:absolute;height:5px;width:42px;background:var(--red)}
.btn{position:absolute;display:flex;align-items:center;justify-content:center;font-family:"Poppins",Arial,sans-serif;font-weight:600;font-size:15px;text-transform:uppercase;color:var(--white)}
.btn-red{background:var(--red)}
.btn-outline{border:2px solid var(--white)}

/* header */
.site-header{position:absolute;left:0;top:0;width:1200px;height:97px;background:var(--white);border-top:4px solid var(--red)}
.brand{position:absolute;left:110px;top:22px;font-family:"Poppins",Arial,sans-serif;font-weight:700;color:var(--ink);line-height:1}
.brand .name{font-size:44px;letter-spacing:1px}
.brand .sub{font-size:15px;margin-top:2px;padding-left:22px}
.social{position:absolute;top:8px;display:flex;gap:13px;left:913px}
.social span{width:34px;height:34px;border-radius:50%;background:var(--red)}
.nav{position:absolute;top:64px;left:659px;display:flex;gap:25px;font-family:"Poppins",Arial,sans-serif;font-weight:600;font-size:14px;color:var(--ink)}

/* hero */
.hero{position:absolute;left:0;top:97px;width:1200px;height:600px;background:linear-gradient(180deg,#2b2f3a 0%,#5a4236 45%,#3a2a24 100%)}
.hero-title{position:absolute;top:180px;width:100%;text-align:center;font-family:"Poppins",Arial,sans-serif;font-weight:700;font-size:42px;color:var(--white)}
.hero-text{position:absolute;top:265px;width:100%;text-align:center;font-size:14.5px;line-height:30px;color:#eee}
.arrow{position:absolute;top:280px}

/* about */
.about-title{left:66px;top:782px;font-size:34px;line-height:42px}
.about-text{left:66px;top:906px;width:470px;font-size:13.2px;line-height:30px;color:#333}
.about-photo{left:622px;top:790px;width:458px;height:493px;border-radius:14px;background:linear-gradient(160deg,#6b4a38,#2a2322 60%,#171515)}

/* menu */
.menu{position:absolute;left:0;top:1418px;width:1200px;height:667px;background:linear-gradient(180deg,#d41a38,#c40b27)}
.menu .title{position:absolute;top:74px;width:100%;text-align:center;font-family:"Poppins",Arial,sans-serif;font-weight:700;font-size:34px;color:var(--white)}
.menu .bar{position:absolute;left:579px;top:137px;width:42px;height:6px;background:var(--white)}
.dish{position:absolute;top:185px;width:223px;height:240px;border-radius:12px}
.dish-caption{position:absolute;top:475px;width:260px;text-align:center;font-family:"Poppins",Arial,sans-serif;font-weight:600;font-size:16px;color:var(--white)}

/* gift cards */
.gift{position:absolute;left:0;top:2085px;width:1200px;height:500px;background:var(--grey)}
.coupon{position:absolute;top:185px;width:390px;height:207px;border:1.5px dashed var(--red)}
.coupon .card{position:absolute;left:25px;top:15px;width:338px;height:176px;background:var(--red)}
.coupon .deal{position:absolute;top:14px;font-family:"Poppins",Arial,sans-serif;font-weight:600;font-size:43px;color:var(--white)}
.coupon .fine{position:absolute;top:82px;width:160px;font-family:"Poppins",Arial,sans-serif;font-size:11px;line-height:24px;color:var(--white)}
.coupon .food{position:absolute;top:0;width:150px;height:176px}

/* contact form */
.field{position:absolute;border:1px solid #999;border-radius:4px;background:var(--white);font-family:"Poppins",Arial,sans-serif;font-size:12.5px;color:#444;padding:14px 18px}

/* gallery */
.tile{position:absolute;top:3137px;width:240px;height:295px}

/* footer */
.footer{position:absolute;left:0;top:3445px;width:1200px;height:412px;background:var(--footer);color:#eee}
.footer h4{position:absolute;top:72px;font-family:"Poppins",Arial,sans-serif;font-weight:600;font-size:16px;color:var(--white)}
.footer h4::after{content:"";position:absolute;left:0;top:30px;width:85px;height:2px;background:var(--red)}
.footer ul{position:absolute;top:115px;list-style:none;font-size:14.5px;line-height:30px}
.footer li::before{content:"»";margin-right:16px}
.f-brand{position:absolute;left:110px;top:100px;font-family:"Poppins",Arial,sans-serif;font-weight:700;line-height:1;color:var(--white)}
.f-brand .name{font-size:46px;letter-spacing:1px}
.f-brand .sub{font-size:15px;margin-top:2px;padding-left:24px}
.f-about{position:absolute;left:107px;top:178px;width:285px;font-size:14.5px;line-height:30px}
.contact-row{position:absolute;left:867px;display:flex;gap:14px;font-size:14.5px;line-height:30px}
.contact-row svg{flex:none;margin-top:8px}
.f-social{position:absolute;left:875px;top:289px;display:flex;gap:12px}
.f-social span{width:12px;height:12px;border-radius:50%;background:var(--white)}
.f-line{position:absolute;left:115px;top:343px;width:970px;height:1px;background:#777}
.copy{position:absolute;top:352px;width:100%;text-align:center;font-size:13.5px}
</style>
</head>
<body>

<header class="site-header">
  <div class="brand"><div class="name">BRAVA</div><div class="sub">Stone Oven Kitchen</div></div>
  <div class="social" aria-label="Social links"><span></span><span></span><span></span><span></span></div>
  <nav class="nav"><span>HOME</span><span>ABOUT US</span><span>GIFT CARDS</span><span>MENU</span><span>CONTACT US</span></nav>
</header>

<section class="hero">
  <div class="abs" role="img" aria-label="Street view of the brick restaurant building at dusk" style="inset:0;background:linear-gradient(180deg,rgba(20,24,34,.35),rgba(20,14,12,.45))"></div>
  <svg class="arrow" style="left:60px" width="16" height="24" viewBox="0 0 16 24"><path d="M12 3 4 12l8 9" fill="none" stroke="#fff" stroke-width="3"/></svg>
  <svg class="arrow" style="left:1124px" width="16" height="24" viewBox="0 0 16 24"><path d="M4 3l8 9-8 9" fill="none" stroke="#fff" stroke-width="3"/></svg>
  <h1 class="hero-title">INNER IDEAS? HOW ABOUT BRAVA!</h1>
  <p class="hero-text">Lorem ipsum dolor sit amet, consectetur adipiscing elit, sed do eiusmod tempor incididunt ut labore et dolore magna aliqua.<br>Quis ipsum suspendisse ultrices gravida. Risus commodo viverra maecenas accumsan lacus vel facilisis.</p>
  <div class="btn btn-outline" style="left:411px;top:353px;width:180px;height:54px">Reservations</div>
  <div class="btn btn-red" style="left:607px;top:353px;width:181px;height:54px">Take Out</div>
</section>

<section>
  <h2 class="heading abs about-title"><span class="accent">About Brava</span> Stone Oven<br>Kitchen</h2>
  <div class="rule" style="left:66px;top:882px"></div>
  <p class="abs about-text">Sed ut perspiciatis unde omnis iste natus error sit voluptatem accusan-tium doloremque laudantium, totam rem aperiam, eaque ipsa quae ab illo inventore veritatis et quasi architecto beatae vitae dicta sunt explicabo. Nemo enim ipsam vluptatem quia voluptas sit aspernatur aut odit aut fugit, sed quia consequuntur magni dolores eos qui ratione voluptatem sequi nesciunt. Neque porro quisquam est, qui dolorem ipsum quia dolor sit amet, consectetur, adipisci velit, sed quia non numquam eius modi tempora incidunt ut labore et dolore magnam aliquam quaerat vo-luptatem. Ut enim ad minima veniam, quis .</p>
  <div class="btn btn-red" style="left:66px;top:1225px;width:181px;height:53px">Learn More</div>
  <div class="abs about-photo" role="img" aria-label="Photo of the restaurant team in front of the stone oven"></div>
  <svg class="abs" style="left:560px;top:735px" width="580" height="600" viewBox="0 0 580 600">
    <rect x="85" y="70" width="420" height="460" rx="10" transform="rotate(-20 295 300)" fill="none" stroke="#d50f25" stroke-width="2"/>
  </svg>
</section>

<section class="menu">
  <div class="abs" role="img" aria-label="Faded red-tinted street view of the restaurant" style="inset:0;background:linear-gradient(180deg,rgba(255,255,255,.04),rgba(0,0,0,.06))"></div>
  <h2 class="title">OUR MENU</h2>
  <div class="bar"></div>

  <div class="dish" style="left:122px;background:linear-gradient(135deg,#c9a27a,#7a5a3a 55%,#e8e2da)" role="img" aria-label="Stone oven pizza topped with greens"></div>
  <div class="dish" style="left:491px;background:linear-gradient(135deg,#6a3a6a,#8a5a2a 55%,#d8c8a8)" role="img" aria-label="Tacos with red cabbage and grilled meat"></div>
  <div class="dish" style="left:859px;background:linear-gradient(180deg,#2a2a2e,#4a3a2a 45%,#7a9a3a)" role="img" aria-label="Pizza served in front of the oven"></div>
  <svg class="abs" style="left:0;top:150px" width="1200" height="320" viewBox="0 0 1200 320">
    <g fill="none" stroke="#fff" stroke-width="2">
      <rect x="110" y="20" width="245" height="260" rx="14" transform="rotate(-15 233 150)"/>
      <rect x="479" y="20" width="245" height="260" rx="14" transform="rotate(-15 602 150)"/>
      <rect x="847" y="20" width="245" height="260" rx="14" transform="rotate(-15 970 150)"/>
    </g>
  </svg>
  <p class="dish-caption" style="left:104px">SED UT PERSPICIATIS</p>
  <p class="dish-caption" style="left:472px">SED UT PERSPICIATIS</p>
  <p class="dish-caption" style="left:840px">SED UT PERSPICIATIS</p>
  <div class="btn btn-outline" style="left:511px;top:527px;width:179px;height:53px">View All Menus</div>
</section>

<section class="gift">
  <h2 class="heading abs" style="top:75px;width:100%;text-align:center;font-size:34px"><span class="accent">Our</span> Gift Cards</h2>
  <div class="rule" style="left:579px;top:130px"></div>

  <div class="coupon" style="left:185px">
    <svg class="abs" style="left:212px;top:-16px" width="36" height="30" viewBox="0 0 36 30"><g fill="none" stroke="#222" stroke-width="2"><circle cx="6" cy="7" r="4"/><circle cx="6" cy="23" r="4"/><path d="M10 9l24 12M10 21l24-12"/></g></svg>
    <div class="card">
      <div class="deal" style="left:15px">50% off</div>
      <p class="fine" style="left:16px">Lorem ipsum dolor sit amet, consectetur adipiscing elit, sed do eiusmod tem.</p>
      <div class="food" style="right:0;background:linear-gradient(90deg,#d50f25,#9a6a48 40%,#e0d4c4)" role="img" aria-label="Rolled porchetta on a plate"></div>
    </div>
  </div>
  <div class="coupon" style="left:625px">
    <svg class="abs" style="left:218px;top:-16px" width="36" height="30" viewBox="0 0 36 30"><g fill="none" stroke="#222" stroke-width="2"><circle cx="30" cy="7" r="4"/><circle cx="30" cy="23" r="4"/><path d="M26 9 2 21M26 21 2 9"/></g></svg>
    <div class="card">
      <div class="food" style="left:0;background:linear-gradient(90deg,#c8a060,#6a8a3a 50%,#d50f25)" role="img" aria-label="Burger held in hand"></div>
      <div class="deal" style="left:160px">50% off</div>
      <p class="fine" style="left:163px">Lorem ipsum dolor sit amet, consectetur adipiscing elit, sed do eiusmod tem.</p>
    </div>
  </div>
</section>

<section>
  <h2 class="heading abs" style="top:2660px;width:100%;text-align:center;font-size:34px"><span class="accent">Get</span> In Touch</h2>
  <div class="rule" style="left:579px;top:2715px"></div>
  <div class="field" style="left:202px;top:2745px;width:392px;height:46px">First name</div>
  <div class="field" style="left:606px;top:2745px;width:392px;height:46px">Last name</div>
  <div class="field" style="left:202px;top:2805px;width:392px;height:46px">Email</div>
  <div class="field" style="left:606px;top:2805px;width:392px;height:46px">Phone</div>
  <div class="field" style="left:202px;top:2866px;width:796px;height:114px">Message</div>
  <div class="btn btn-red" style="left:510px;top:2997px;width:180px;height:53px">Submit</div>
</section>

<section aria-label="Photo gallery">
  <div class="tile" style="left:0;background:linear-gradient(160deg,#c24a2a,#e89a4a 50%,#7a5a3a)" role="img" aria-label="Colourful patio with red umbrellas"></div>
  <div class="tile" style="left:240px;background:linear-gradient(160deg,#5a5a5a,#9a8a5a 50%,#6a8a3a)" role="img" aria-label="Tacos with avocado and lime"></div>
  <div class="tile" style="left:480px;background:linear-gradient(160deg,#e8202e,#d5102a)" role="img" aria-label="Red-tinted food photo with gallery link"></div>
  <div class="abs" style="left:593px;top:3279px;width:14px;height:14px;border-radius:50%;border:1.6px solid #fff"></div>
  <div class="tile" style="left:720px;background:linear-gradient(160deg,#e8e4de,#c8a26a 50%,#8a5a3a)" role="img" aria-label="Pizzas on wooden boards"></div>
  <div class="tile" style="left:960px;background:linear-gradient(160deg,#3a3a3a,#7a4a6a 50%,#c89a5a)" role="img" aria-label="Close-up of tacos"></div>
</section>

<footer class="footer">
  <div class="f-brand"><div class="name">BRAVA</div><div class="sub">Stone Oven Kitchen</div></div>
  <p class="f-about">Lorem ipsum dolor sit amet, consec tetur adipiscing elit, sed do eiusmod tempor incididunt ut labore et aliqua.</p>

  <h4 style="left:430px">QUICK LINKS</h4>
  <ul style="left:432px"><li>Home</li><li>About Us</li><li>Menu</li><li>Gift Cards</li><li>Contact Us</li></ul>

  <h4 style="left:601px">CANADA DAY HOURS!</h4>
  <ul style="left:601px"><li>Thursday, July 1st &nbsp;- &nbsp;Open</li><li>Friday, July 2nd &nbsp;- &nbsp;Open</li><li>Saturday, July 3rd &nbsp;- &nbsp;Open</li><li>Sunday, July 4th &nbsp;- &nbsp;Closed</li></ul>

  <h4 style="left:867px">CONTACT INFO</h4>
  <div class="contact-row" style="top:115px">
    <svg width="12" height="16" viewBox="0 0 12 16"><path d="M6 0a6 6 0 0 0-6 6c0 4.5 6 10 6 10s6-5.5 6-10a6 6 0 0 0-6-6zm0 8.5A2.5 2.5 0 1 1 6 3.5a2.5 2.5 0 0 1 0 5z" fill="#fff"/></svg>
    <span>48 Alder Row<br>Linwell, ON</span>
  </div>
  <div class="contact-row" style="top:193px">
    <svg width="14" height="14" viewBox="0 0 14 14"><path d="M3 0 5 4 3.5 5.5a9 9 0 0 0 5 5L10 9l4 2-1 3C6 14 0 8 0 1z" fill="#fff"/></svg>
    <span>555-014-2287</span>
  </div>
  <div class="contact-row" style="top:236px">
    <svg width="15" height="12" viewBox="0 0 15 12"><rect width="15" height="12" rx="1.5" fill="#fff"/><path d="M1 1.5 7.5 7 14 1.5" fill="none" stroke="#1f1f1f" stroke-width="1.4"/></svg>
    <span>hello@bravalinwell.example</span>
  </div>
  <div class="f-social" aria-label="Social links"><span></span><span></span><span></span><span></span></div>

  <div class="f-line"></div>
  <p class="copy">© Copyrights 2021 Brava &nbsp; | &nbsp; All Rights Reserved</p>
</footer>

</body>
</html>
```